Bref créative
Wedding photographer business card
and stationary
Bright & Fun-filled
Lora Bexley
no address needed
lorabexley@mailvista.net
www.lorabexley.net
I like sleek but also fun and feminine.
corrected phone number given to winning designer for finalizing design.
Thanks
Special offer,
$50 off,
a package & a free 8x10 print
I have two designs so you may choose either logo to design.
here's the monogram for my second logo
the flowers for logo 2

```html
<!DOCTYPE html>
<html lang="en">
<head>
<meta charset="utf-8">
<title>Lora Bexley Photography – Business Card</title>
<link rel="stylesheet" href="https://fonts.googleapis.com/css2?family=Open+Sans:wght@400;600;700;800&display=swap">
<style>
  :root {
    --page-bg: #ece6df;
    --card-front: #ffffff;
    --card-back: #b3a395;
    --brand-brown: #5a4037;
    --accent-pink: #e04a78;
    --text-light: #ffffff;
    --decor-tone: #c9b8aa;
    --divider: rgba(255,255,255,0.55);
  }
  * { margin: 0; padding: 0; box-sizing: border-box; }
  html, body { width: 1200px; height: 901px; overflow: hidden; }
  body {
    background: var(--page-bg);
    font-family: "Open Sans", Arial, sans-serif;
    position: relative;
  }
  .card {
    position: absolute;
    top: 300px;
    width: 520px;
    height: 300px;
    border-radius: 22px;
    box-shadow: 0 6px 18px rgba(60,40,30,0.18);
    overflow: hidden;
  }
  .card--front { left: 50px; background: var(--card-front); }
  .card--back { left: 630px; background: var(--card-back); }

  .brand {
    position: absolute;
    left: 0; right: 0; top: 118px;
    display: flex; align-items: center; justify-content: center; gap: 16px;
  }
  .brand__dot { width: 22px; height: 22px; border-radius: 50%; background: var(--accent-pink); }
  .brand__name {
    font-size: 46px; font-weight: 600; color: var(--brand-brown); letter-spacing: 1px;
  }

  .offer {
    position: absolute; left: 24px; top: 34px; width: 290px; text-align: center;
    color: var(--text-light);
  }
  .offer__title { font-size: 30px; font-weight: 800; letter-spacing: 1px; }
  .offer__amount { font-size: 28px; font-weight: 700; margin-top: 2px; }
  .offer__detail { font-size: 18px; font-weight: 600; margin-top: 8px; white-space: nowrap; }

  .decor {
    position: absolute; right: 40px; top: 24px; width: 150px; height: 140px;
    border-radius: 50%; background: var(--decor-tone); opacity: 0.55;
  }

  .divider {
    position: absolute; left: 292px; top: 170px; width: 1px; height: 100px;
    background: var(--divider);
  }
  .contact {
    position: absolute; left: 308px; top: 172px; width: 190px; color: var(--text-light);
    font-size: 12px; list-style: none;
  }
  .contact__name { font-weight: 700; margin-bottom: 8px; font-size: 13px; }
  .contact__item { display: flex; align-items: center; gap: 7px; margin-bottom: 6px; white-space: nowrap; }
  .contact__icon { width: 12px; height: 12px; flex: none; }

  .back-brand {
    position: absolute; left: 60px; top: 212px;
    display: flex; align-items: center; gap: 10px;
  }
  .back-brand__dot { width: 14px; height: 14px; border-radius: 50%; background: var(--accent-pink); }
  .back-brand__name { font-size: 26px; font-weight: 600; color: var(--text-light); }
</style>
</head>
<body>
  <section class="card card--front" aria-label="Business card front">
    <div class="brand">
      <span class="brand__dot"></span>
      <span class="brand__name">Lora Bexley</span>
    </div>
  </section>

  <section class="card card--back" aria-label="Business card back">
    <div class="decor" role="img" aria-label="Faint floral decoration"></div>
    <div class="offer">
      <p class="offer__title">SPECIAL OFFER</p>
      <p class="offer__amount">50$off</p>
      <p class="offer__detail">a package and a free 8x10 print</p>
    </div>
    <div class="back-brand">
      <span class="back-brand__dot"></span>
      <span class="back-brand__name">Lora Bexley</span>
    </div>
    <div class="divider"></div>
    <ul class="contact">
      <li class="contact__name">Lora Bexley</li>
      <li class="contact__item">
        <svg class="contact__icon" viewBox="0 0 12 12"><circle cx="6" cy="6" r="6" fill="#e04a78"/><path d="M4 3.2 5 3l.8 1.6-.7.6a4 4 0 0 0 1.7 1.7l.6-.7L9 7l-.2 1c-2.8.2-5-2-4.8-4.8z" fill="#fff"/></svg>
        555-014-2288
      </li>
      <li class="contact__item">
        <svg class="contact__icon" viewBox="0 0 12 12"><circle cx="6" cy="6" r="6" fill="#e04a78"/><rect x="3" y="4" width="6" height="4" fill="none" stroke="#fff" stroke-width="0.9"/><path d="M3 4l3 2.2L9 4" fill="none" stroke="#fff" stroke-width="0.9"/></svg>
        lorabexley@mailvista.net
      </li>
      <li class="contact__item">
        <svg class="contact__icon" viewBox="0 0 12 12"><circle cx="6" cy="6" r="6" fill="#e04a78"/><circle cx="6" cy="6" r="3" fill="none" stroke="#fff" stroke-width="0.9"/><path d="M3 6h6M6 3v6" stroke="#fff" stroke-width="0.7"/></svg>
        www.lorabexley.net
      </li>
    </ul>
  </section>
</body>
</html>
```